WHAT LIES BEYOND? Discovering the shape of days with the Silent Lamp

Creating a book that is about living a spiritual life. The book is about letting go of the materialistic world and finding happiness through self realisation and enlightenment. The contents page is below that gives an idea of what is contained in the book.

The book is based on the writings of the Sikhs - from India. But it is written in a universal way that is understandable to all.

CONTENTS
Living for a purpose
- Born to be original! Dying as a copy!
- My relationship with everything but me!
- What is my purpose?

Life as a human being!
- Stages of Life
- Five Weaknesses

What is driving our lives?
- Information overload?
- What are your drivers?
- Giving life meaning

You reap what you sow
- Is my destiny written?
- Good and bad actions
- Maya – the illusion and it’s three modes

Slow down and let go
- The mind in overdrive
- Being aware of our mental health
- Why Slow Down?

The Guidance of the Guru
- Why do I need a Guru?
- What the Guru gives you
- Gurbani – the Guru’s Words

Staying connected
- Repeating the Mantra
- Doing two things at once
- Remembering in times of difficulty

Cultivating virtues
- Theory vs Practice
- Virtues and true religion
- Some key virtues

The Mystical Creation
- Experiencing ecstasy
- Enlightenment and intuition
- Spiritual Transformation

Good Company
- How do my companions affect me?
- The company of Saintly people
- Obtaining the fruits that the Guru describes

Serving selflessly
- Serving is our purpose
- Being grateful
- Being generous

Ten things to change your life today

Target Market(s)

All those who want to learn about spirituality. We are targeting young and middle aged but not necessarily ruling out older demographic.

Requirements
Must have
• The book cover:

- exciting and intriguing
- theme is "what lies beyond" in this world
- some kind of lean towards enlightenment
Nice to have
• It is not essential but the cover could subtly show something about the Sikh faith. Can discuss this further if necessary.
Should not have
• Should not:

- look dull and boring
- don't want it to look like a Buddhism book

```html
<!DOCTYPE html>
<html lang="en">
<head>
<meta charset="utf-8">
<title>What Lies Beyond? – Book Cover Spread</title>
<link rel="stylesheet" href="https://fonts.googleapis.com/css2?family=EB+Garamond:ital,wght@0,400;0,500;0,700;1,400;1,700&display=swap">
<style>
  :root {
    --orange: #f14d12;
    --orange-box: #ff4a05;
    --ink: #1a1612;
    --paper: #ffffff;
    --mist: #ededed;
    --sand: #e3c17f;
  }
  * { margin: 0; padding: 0; box-sizing: border-box; }
  html, body { width: 1200px; height: 900px; overflow: hidden; background: var(--paper); }
  body { font-family: "EB Garamond", Georgia, serif; color: var(--ink); }

  .spread { position: relative; width: 1200px; height: 900px; overflow: hidden; }

  /* panels */
  .back-cover { position: absolute; left: 0; top: 0; width: 570px; height: 900px; background: var(--paper); }
  .spine { position: absolute; left: 570px; top: 0; width: 60px; height: 900px; background: var(--mist); }
  .front-cover { position: absolute; left: 630px; top: 0; width: 570px; height: 900px; background: var(--mist); overflow: hidden; }
  .base-band { position: absolute; left: 0; top: 806px; width: 1200px; height: 94px; background: var(--sand); }

  /* back cover */
  .back-title {
    position: absolute; left: 0; top: 38px; width: 570px; text-align: center;
    font-size: 44px; font-weight: 400; color: var(--orange); letter-spacing: 1px; line-height: 1;
  }
  .back-subtitle {
    position: absolute; left: 0; top: 100px; width: 570px; text-align: center;
    font-style: italic; font-size: 20px;
  }
  .back-subtitle strong, .front-subtitle strong { font-weight: 700; }
  .contents-heading {
    position: absolute; left: 0; top: 182px; width: 570px; text-align: center;
    font-size: 20px; font-weight: 500;
  }
  .contents-column {
    position: absolute; top: 236px; width: 290px; text-align: center;
    font-size: 15.5px; line-height: 16.67px; letter-spacing: -0.2px;
  }
  .contents-column.left { left: 13px; }
  .contents-column.right { left: 276px; }
  .chapter { margin-bottom: 16.67px; }
  .chapter-title { font-weight: 500; }
  .barcode-area {
    position: absolute; left: 342px; top: 737px; width: 200px; height: 120px;
    background: var(--orange-box); z-index: 2;
  }

  /* spine */
  .spine-title, .spine-author {
    position: absolute; left: 30px; white-space: nowrap;
    transform-origin: 0 0; transform: rotate(90deg);
  }
  .spine-title { top: 34px; font-size: 29px; color: var(--orange); letter-spacing: 1px; margin-left: 16px; }
  .spine-author { top: 656px; font-size: 25px; font-variant: small-caps; margin-left: 14px; z-index: 2; }

  /* front cover */
  .emblem-glow {
    position: absolute; left: 150px; top: 50px; width: 260px; height: 250px;
    background: radial-gradient(ellipse at center, rgba(238,220,170,0.55) 0%, rgba(238,220,170,0.25) 45%, rgba(237,237,237,0) 72%);
  }
  .front-title {
    position: absolute; left: 0; top: 22px; width: 570px; text-align: center;
    color: var(--orange); font-weight: 400; line-height: 1;
  }
  .front-title .title-main { display: block; font-size: 132px; letter-spacing: -2px; }
  .front-title .title-rest { display: block; font-size: 56px; margin-top: 4px; letter-spacing: 1px; }
  .front-subtitle {
    position: absolute; left: 0; top: 262px; width: 570px; text-align: center;
    font-style: italic; font-size: 30px; line-height: 40px;
  }
  .cover-photo {
    position: absolute; left: 0; top: 360px; width: 570px; height: 446px;
    background:
      linear-gradient(180deg, var(--mist) 0%, rgba(237,237,237,0) 22%),
      radial-gradient(ellipse at 30% 45%, rgba(120,140,95,0.75), rgba(120,140,95,0) 55%),
      radial-gradient(ellipse at 85% 40%, rgba(225,150,185,0.8), rgba(225,150,185,0) 50%),
      radial-gradient(ellipse at 92% 78%, rgba(240,120,40,0.8), rgba(240,120,40,0) 35%),
      radial-gradient(ellipse at 55% 85%, rgba(210,195,185,0.95), rgba(210,195,185,0) 60%),
      linear-gradient(180deg, #cfd2c4 0%, #b9b79e 45%, #d8ccc4 100%);
  }
  .front-author {
    position: absolute; left: 0; top: 812px; width: 570px; text-align: center;
    font-size: 44px; font-variant: small-caps; letter-spacing: 0.5px; z-index: 2;
  }
</style>
</head>
<body>
<main class="spread">
  <section class="back-cover">
    <h2 class="back-title">WHAT LIES BEYOND?</h2>
    <p class="back-subtitle">Discovering the shape of days with the <strong>Silent Lamp</strong></p>
    <h3 class="contents-heading">Contents</h3>

    <div class="contents-column left">
      <div class="chapter"><div class="chapter-title">Living for a purpose</div>
        <div>- Born to be original! Dying as a copy!</div>
        <div>- My relationship with everything but me!</div>
        <div>- What is my purpose?</div></div>
      <div class="chapter"><div class="chapter-title">Life as a human being!</div>
        <div>- Stages of Life</div>
        <div>- Five Weaknesses</div></div>
      <div class="chapter"><div class="chapter-title">What is driving our lives?</div>
        <div>- Information overload?</div>
        <div>- What are your drivers?</div>
        <div>- Giving life meaning</div></div>
      <div class="chapter"><div class="chapter-title">You reap what you sow</div>
        <div>- Is my destiny written?</div>
        <div>- Good and bad actions</div>
        <div>- Maya – the illusion and it’s three modes</div></div>
      <div class="chapter"><div class="chapter-title">Slow down and let go</div>
        <div>- The mind in overdrive</div>
        <div>- Being aware of our mental health</div>
        <div>- Why Slow Down?</div></div>
      <div class="chapter"><div class="chapter-title">The Guidance of the Guru</div>
        <div>- Why do I need a Guru?</div>
        <div>- What the Guru gives you</div>
        <div>- Gurbani – the Guru’s Words</div></div>
    </div>

    <div class="contents-column right">
      <div class="chapter"><div class="chapter-title">Staying connected</div>
        <div>- Repeating the Mantra</div>
        <div>- Doing two things at once</div>
        <div>- Remembering in times of difficulty</div></div>
      <div class="chapter"><div class="chapter-title">Cultivating virtues</div>
        <div>- Theory vs Practice</div>
        <div>- Virtues and true religion</div>
        <div>- Some key virtues</div></div>
      <div class="chapter"><div class="chapter-title">The Mystical Creation</div>
        <div>- Experiencing ecstasy</div>
        <div>- Enlightenment and intuition</div>
        <div>- Spiritual Transformation</div></div>
      <div class="chapter"><div class="chapter-title">Good Company</div>
        <div>- How do my companions affect me?</div>
        <div>- The company of Saintly people</div>
        <div>- Obtaining the fruits that the Guru</div>
        <div>describes</div></div>
      <div class="chapter"><div class="chapter-title">Serving selflessly</div>
        <div>- Serving is our purpose</div>
        <div>- Being grateful</div>
        <div>- Being generous</div></div>
      <div class="chapter"><div class="chapter-title">Ten things to change your life today</div></div>
    </div>

    <div class="barcode-area"></div>
  </section>

  <section class="spine">
    <div class="spine-title">WHAT LIES BEYOND?</div>
    <div class="spine-author">Author’s Name</div>
  </section>

  <section class="front-cover">
    <div class="emblem-glow" role="img" aria-label="Faint golden faith emblem glowing behind the title"></div>
    <h1 class="front-title">
      <span class="title-main">WHAT</span>
      <span class="title-rest">LIES BEYOND?</span>
    </h1>
    <p class="front-subtitle">Discovering the shape of<br>days with the <strong>Silent Lamp</strong></p>
    <div class="cover-photo" role="img" aria-label="Photograph of four joyful young men in white, dusted with coloured powder, raising their arms with a drum and tambourine among trees and pink colour clouds"></div>
  </section>

  <div class="base-band"></div>
  <div class="front-author" style="left:630px;">Author’s Name</div>
</main>
</body>
</html>
```